Business Card Trevian Digital

Design of two business cards (board) for Trevian Digital. Trevian Digital DMCC, based in in Dubai U.A.E. Trevian Digital is a self-contained online company, taking an online concept from idea to reality. Concretely, this has involved the (partly remote) management, website development, market implementation and mobile application development for several platforms.

Frontside of business card should feature our company logo (Trevian) and personal details. Backside should feature the logo's of our current brands (mendquickly, taskpalace and galaplanner). We would prefer a design based on the grey/orange color scheme of our company. Trevian Digital is a young, modern and dynamic company and we would like to see this reflected in the design.

```html
<!DOCTYPE html>
<html lang="en">
<head>
<meta charset="utf-8">
<title>Trevian Digital – Business Card</title>
<link href="https://fonts.googleapis.com/css2?family=Saira:wght@400;500&display=swap" rel="stylesheet">
<style>
  :root {
    --stage: #dcdee6;
    --card-white: #f4f4f4;
    --panel-grey: #58585a;
    --band-dark: #333335;
    --accent-orange: #ee6338;
    --ink-light: #ffffff;
  }
  * { margin: 0; padding: 0; box-sizing: border-box; }
  html, body {
    width: 1200px; height: 840px; overflow: hidden;
    background: var(--stage);
    font-family: "Saira", sans-serif;
  }
  .business-card {
    position: absolute; left: 100px; top: 134px;
    width: 1000px; height: 571px;
    background: var(--card-white);
    box-shadow: 0 10px 30px rgba(0,0,0,0.18);
    overflow: hidden;
  }
  .card-shapes { position: absolute; inset: 0; width: 100%; height: 100%; }
  .brand {
    position: absolute; left: 150px; top: 400px;
    display: flex; align-items: center; gap: 22px;
  }
  .brand-dot {
    width: 74px; height: 74px; border-radius: 50%;
    background: var(--panel-grey);
  }
  .brand-name {
    color: var(--accent-orange);
    font-size: 46px; font-weight: 400; letter-spacing: 9px;
  }
  .contact-block {
    position: absolute; right: 40px; top: 34px;
    text-align: right; color: var(--ink-light);
  }
  .person-name { font-size: 30px; font-weight: 500; letter-spacing: 2px; line-height: 1.1; }
  .person-role { font-size: 18px; letter-spacing: 1.5px; margin-top: 2px; }
  .address { font-size: 23px; line-height: 1.3; margin-top: 46px; }
  .contact-list { list-style: none; margin-top: 36px; }
  .contact-list li {
    display: flex; justify-content: flex-end; align-items: center; gap: 14px;
    font-size: 21px; letter-spacing: 1px; height: 38px;
  }
  .contact-list svg { width: 22px; height: 22px; fill: none; stroke: var(--ink-light); stroke-width: 1.8; }
  .contact-list svg .solid { fill: var(--ink-light); stroke: none; }
</style>
</head>
<body>
  <div class="business-card">
    <svg class="card-shapes" viewBox="0 0 1000 571" preserveAspectRatio="none" aria-hidden="true">
      <path class="edge-band" d="M350,0 C480,20 585,120 585,300 L585,571 L1000,571 L1000,0 Z" fill="var(--band-dark)"/>
      <path class="accent-wedge" d="M378,0 C500,26 594,130 594,345 C602,200 590,80 536,0 Z" fill="var(--accent-orange)"/>
      <path class="info-panel" d="M548,0 C596,80 604,200 604,345 L604,571 L1000,571 L1000,0 Z" fill="var(--panel-grey)" stroke="var(--band-dark)" stroke-width="6"/>
    </svg>

    <div class="brand">
      <div class="brand-dot"></div>
      <div class="brand-name">TREVIAN</div>
    </div>

    <div class="contact-block">
      <div class="person-name">DANIEL CORVELL</div>
      <div class="person-role">FINANCIAL ADVISOR</div>
      <div class="address">041.12th floor,Bay<br>Harbour Road DXB</div>
      <ul class="contact-list">
        <li>014 275 3390
          <svg viewBox="0 0 24 24"><path class="solid" d="M6 3l3 0 1.5 4-2 1.5c1 2.3 2.7 4 5 5l1.5-2 4 1.5v3c0 1-1 2-2 2C10 18 6 14 4 7c0-1 1-2 2-2z"/></svg>
        </li>
        <li>014 275 3391
          <svg viewBox="0 0 24 24"><rect x="7" y="2" width="10" height="20" rx="2"/><line x1="11" y1="18.5" x2="13" y2="18.5"/></svg>
        </li>
        <li>014 275 3392
          <svg viewBox="0 0 24 24"><rect x="4" y="9" width="16" height="12"/><rect x="7" y="3" width="10" height="6"/><line x1="8" y1="13" x2="16" y2="13"/><line x1="8" y1="17" x2="16" y2="17"/></svg>
        </li>
        <li>dcorvell@trevian.io
          <svg viewBox="0 0 24 24"><rect x="3" y="5" width="18" height="14"/><polyline points="3,5 12,13 21,5"/></svg>
        </li>
        <li>www.treviandigital.net
          <svg viewBox="0 0 24 24"><circle cx="12" cy="12" r="9"/><ellipse cx="12" cy="12" rx="4" ry="9"/><line x1="3" y1="12" x2="21" y2="12"/></svg>
        </li>
      </ul>
    </div>
  </div>
</body>
</html>
```